Poster & Banner for Outback tour company

Poster needed for tour company in the Australian outback. We will need it in an A2 format and if possible a larger banner format as Well please. It needs the Kestrel Tours logo but also the other logos (less obvious). It also needs to feature the Vantorix logo (uploaded).

The poster needs a list of the tours we offer as well as some of the pictures uploaded.

List of tours:

- Deluxe Tour of the Village and the Redspurs $99
- Marrandi Scenic Tour $85
- Starlight Redspurs Tour $60
- Quartz Trailside Tour $50

Industry/Entity Type

Tour Company

Font styles to use
Serif

Colors

Designer to choose colors to be used in the design.

Requirements
Must have
• Kestrel Tours logo/List of tours/

```html
<!DOCTYPE html>
<html lang="en">
<head>
<meta charset="utf-8">
<title>Kestrel Tours Australia – Poster</title>
<link href="https://fonts.googleapis.com/css2?family=Oswald:wght@400;500;600&display=swap" rel="stylesheet">
<style>
  :root {
    --page: #ffffff;
    --cream: #fbf3e1;
    --cream-deep: #f5e7c8;
    --brown: #4a2a14;
    --rust: #a4571d;
    --orange: #d0761d;
    --red: #a8141b;
    --rule: #d9c7a3;
    --green: #3a9a5a;
  }
  * { margin: 0; padding: 0; box-sizing: border-box; }
  html, body { width: 934px; height: 1200px; overflow: hidden; background: var(--page); }
  body { position: relative; font-family: "Oswald", "Arial Narrow", sans-serif; }

  .poster {
    position: absolute; left: 41px; top: 0; width: 852px; height: 1200px;
    background: linear-gradient(180deg, var(--cream) 0%, #fdf6e8 100%);
    overflow: hidden;
  }
  .photo { position: absolute; top: 46px; height: 453px; width: 178px; }
  .photo--hills { left: 13px; background: linear-gradient(180deg, #3f8fd0 0%, #9fc4dc 14%, #c57a3f 30%, #b8562a 60%, #8c3a1d 100%); }
  .photo--cave { left: 201px; background: radial-gradient(circle at 55% 25%, #f3d5a8 0%, #b56027 30%, #7a2e10 75%, #4a1a08 100%); }
  .photo--sign { left: 392px; background: linear-gradient(180deg, #2f6fc4 0%, #6e9fd4 35%, #b6a27a 60%, #6d5a3c 100%); }
  .photo--chapel { left: 581px; background: linear-gradient(180deg, #e8c995 0%, #d39a55 40%, #b5602c 75%, #c98a4a 100%); }

  .map {
    position: absolute; left: 37px; top: 300px; width: 705px; height: 400px;
    background: linear-gradient(180deg, #f8ecd2 0%, var(--cream-deep) 100%);
    border-radius: 120px 160px 140px 90px / 90px 140px 160px 110px;
    box-shadow: 0 6px 14px rgba(120, 80, 30, 0.22);
  }

  .brand { position: absolute; left: 0; width: 852px; top: 528px; text-align: center; color: var(--brown); }
  .brand__mark { display: inline-block; width: 34px; height: 34px; background: var(--orange); border-radius: 4px; margin-bottom: 6px; }
  .brand__name { font-size: 50px; font-weight: 600; line-height: 1; letter-spacing: 0.5px; }
  .brand__sub { font-size: 26px; font-weight: 500; letter-spacing: 12px; color: var(--rust); margin-top: 4px; padding-left: 12px; }

  .section-title {
    position: absolute; top: 692px; left: 0; width: 852px; text-align: center;
    font-size: 24px; font-weight: 600; letter-spacing: 5px; color: var(--rust);
  }
  .rule { position: absolute; left: 303px; width: 245px; height: 1px; background: var(--rule); }
  .rule--top { top: 741px; }
  .rule--bottom { top: 1062px; }

  .tour { position: absolute; }
  .tour__name { font-size: 21px; font-weight: 600; line-height: 1.15; color: var(--orange); }
  .tour__price { font-size: 46px; font-weight: 600; line-height: 1; color: var(--red); margin-top: 6px; }
  .tour__price sup { font-size: 22px; vertical-align: top; position: relative; top: 4px; margin-right: 2px; }
  .tour--left { right: 558px; text-align: right; }
  .tour--right { left: 517px; text-align: left; }
  .tour--row1 { top: 773px; }
  .tour--row2 { top: 910px; }

  .thumb { position: absolute; width: 104px; height: 118px; }
  .thumb--rig { left: 311px; top: 773px; background: linear-gradient(180deg, #2d3a6b 0%, #8b5a7a 45%, #e07a2a 75%, #1c120c 100%); }
  .thumb--glasses { left: 438px; top: 773px; background: linear-gradient(180deg, #5a3a2a 0%, #b87045 50%, #7a4a30 100%); }
  .thumb--dunes { left: 311px; top: 910px; background: linear-gradient(180deg, #2e6fc0 0%, #c7d8e8 22%, #c98a57 45%, #9a4a25 100%); }
  .thumb--truck { left: 438px; top: 910px; background: linear-gradient(180deg, #c97f42 0%, #a45a2a 55%, #e8e2da 75%, #7a4b2a 100%); }

  .partners {
    position: absolute; top: 1109px; left: 0; width: 852px; height: 42px;
    display: flex; justify-content: center; align-items: center; gap: 12px;
  }
  .partners__divider { width: 1px; height: 36px; background: var(--rule); }
  .badge--square { width: 34px; height: 40px; background: var(--green); }
  .badge--circle { width: 42px; height: 42px; border-radius: 50%; background: #d98a2a; }
  .partner-name { font-size: 17px; font-weight: 500; line-height: 1; }
  .partner-name--ridgeline { color: #1f5fa8; }
  .partner-name--parkway { color: #6fa83a; font-size: 14px; }
  .partner-name--clay { color: #c4581e; font-size: 18px; }
</style>
</head>
<body>
  <main class="poster">
    <div class="photo photo--hills" role="img" aria-label="Photo of layered desert hills under a blue sky"></div>
    <div class="photo photo--cave" role="img" aria-label="Photo of an underground sandstone cave tunnel"></div>
    <div class="photo photo--sign" role="img" aria-label="Photo of a roadside opal sign with a painted car"></div>
    <div class="photo photo--chapel" role="img" aria-label="Photo of an underground church interior"></div>

    <div class="map" role="img" aria-label="Cream outline map of Australia"></div>

    <header class="brand">
      <span class="brand__mark"></span>
      <h1 class="brand__name">KESTREL TOURS</h1>
      <p class="brand__sub">AUSTRALIA</p>
    </header>

    <h2 class="section-title">PRESENT TOURS</h2>
    <div class="rule rule--top"></div>

    <div class="tour tour--left tour--row1">
      <p class="tour__name">Deluxe Tour<br>of the Village<br>and the Redspurs</p>
      <p class="tour__price"><sup>$</sup>99</p>
    </div>
    <div class="thumb thumb--rig" role="img" aria-label="Photo of a mining rig silhouetted at sunset"></div>
    <div class="thumb thumb--glasses" role="img" aria-label="Photo of two sparkling wine glasses on red earth"></div>
    <div class="tour tour--right tour--row1" style="left:558px">
      <p class="tour__name">Starlight Redspurs<br>Tour</p>
      <p class="tour__price" style="margin-top:32px"><sup>$</sup>60</p>
    </div>

    <div class="tour tour--left tour--row2">
      <p class="tour__name">Marrandi<br>Scenic Tour</p>
      <p class="tour__price" style="margin-top:24px"><sup>$</sup>85</p>
    </div>
    <div class="thumb thumb--dunes" role="img" aria-label="Photo of striped desert hills"></div>
    <div class="thumb thumb--truck" role="img" aria-label="Photo of a tour truck by a sandstone cliff"></div>
    <div class="tour tour--right tour--row2" style="left:558px">
      <p class="tour__name">Quartz Trailside<br>Tour</p>
      <p class="tour__price" style="margin-top:24px"><sup>$</sup>50</p>
    </div>

    <div class="rule rule--bottom"></div>

    <footer class="partners">
      <span class="badge--square" aria-label="Vantorix badge"></span>
      <span class="partners__divider"></span>
      <span class="badge--circle" aria-label="Partner badge"></span>
      <span class="partners__divider"></span>
      <span class="partner-name partner-name--ridgeline">Ridgeline</span>
      <span class="partners__divider"></span>
      <span class="partner-name partner-name--parkway">Parkway Villages</span>
      <span class="partners__divider"></span>
      <span class="partner-name partner-name--clay">Clay Lodge motel</span>
    </footer>
  </main>
</body>
</html>
```